Mobile Tyre Fitting Business (UK) needs a logo / van livery design 'BRAMBLE PEAK TYRES'

A new business based in the UK 'mobile tyre fitting' The mobile tyre fitting industry in the UK is full of man and van as well as large recognized commercial and franchised brands that we are competing with. Tyre replacement for the customer is costly and a pain and by making it mobile we try to take out the frustration of sitting in a dirty garage waiting for your car, whilst drinking shit coffee. The van is in many ways a mobile HQ, Office, Front of House & Advertising and a Work Horse, and must be presentable as it will be outside the customers house during tyre fittings, as well as advertising the business to passers-by
We are looking for a clean and modern logo design to be used as van-livery deign for a large Norvel Carrack L3/H3 to promote the name and services
As we are mobile, we come to you and you save you time and money
The van is metallic grey
We are looking for clean and modern design that sells mobile tyre fitting along the side and back

Target Market(s)

Tyre Fitting

Industry/Entity Type

Automotive

Font styles to use
Sans Serif

Requirements
Must have
• Company Name 'Bramble Peak Tyres'
'We save you time and money'
Fitters Name 'Declan Hobbs'
Mobile No 'TBC'

```html
<!DOCTYPE html>
<html lang="en">
<head>
<meta charset="utf-8">
<title>Bramble Peak Tyres – Van Livery</title>
<link href="https://fonts.googleapis.com/css2?family=Oswald:wght@500;600&family=Open+Sans:wght@700&display=swap" rel="stylesheet">
<style>
  :root {
    --livery-red: #d0121b;
    --livery-black: #111111;
    --livery-dark: #1f1f1f;
    --livery-white: #f4f4f4;
    --canvas: #ffffff;
    --ink: #111111;
  }
  html, body { margin: 0; padding: 0; overflow: hidden; }
  body { width: 1200px; height: 1200px; background: var(--canvas); position: relative; }
  .brand-mark {
    position: absolute; left: 370px; top: 45px;
    display: flex; align-items: center; gap: 16px;
  }
  .brand-mark__dot { width: 70px; height: 70px; border-radius: 50%; background: var(--livery-red); }
  .brand-mark__name {
    font-family: "Oswald", sans-serif; font-weight: 600; font-size: 52px;
    color: var(--ink); letter-spacing: 0.5px;
  }
  .panel { position: absolute; display: block; }
  .panel--side-left { left: 275px; top: 175px; width: 660px; height: 320px; }
  .panel--side-right { left: 275px; top: 520px; width: 660px; height: 320px; }
  .panel--rear { left: 335px; top: 862px; width: 228px; height: 300px; }
  .panel--front { left: 640px; top: 875px; width: 260px; height: 287px; }
  .t-head { font-family: "Oswald", sans-serif; font-weight: 600; }
  .t-body { font-family: "Open Sans", sans-serif; font-weight: 700; }
</style>
</head>
<body>

<header class="brand-mark">
  <span class="brand-mark__dot"></span>
  <span class="brand-mark__name">BRAMBLE PEAK TYRES</span>
</header>

<!-- Side panel, cab facing left -->
<svg class="panel panel--side-left" viewBox="0 0 660 320" aria-label="Left side livery">
  <rect x="0" y="30" width="660" height="290" rx="24" fill="var(--livery-white)"/>
  <polygon points="200,30 660,0 660,26 260,54" fill="var(--livery-red)"/>
  <polygon points="250,54 660,26 660,66 300,92" fill="var(--livery-black)"/>
  <text class="t-head" x="470" y="65" font-size="14" fill="#fff" letter-spacing="2" text-anchor="middle" transform="rotate(-4 470 65)">WWW.BRAMBLEPEAKTYRES.CO.UK</text>
  <circle cx="190" cy="160" r="30" fill="var(--livery-red)"/>
  <text class="t-head" x="235" y="175" font-size="42" fill="var(--ink)" transform="rotate(-4 235 175)">BRAMBLE PEAK TYRES</text>
  <polygon points="0,250 660,204 660,240 0,286" fill="var(--livery-red)"/>
  <text class="t-body" x="430" y="244" font-size="17" fill="#fff" text-anchor="middle" transform="rotate(-4 430 244)">“We save you time and money”</text>
  <polygon points="0,286 660,240 660,320 0,320" fill="var(--livery-dark)"/>
  <text class="t-head" x="450" y="280" font-size="15" fill="#fff" letter-spacing="1" text-anchor="middle" transform="rotate(-4 450 280)">MOBILE TYRE FITTING</text>
  <text class="t-head" x="40" y="236" font-size="22" fill="var(--livery-red)" transform="rotate(-4 40 236)">07700 <tspan fill="var(--ink)">900 462</tspan></text>
</svg>

<!-- Side panel, cab facing right -->
<svg class="panel panel--side-right" viewBox="0 0 660 320" aria-label="Right side livery">
  <rect x="0" y="0" width="660" height="320" rx="24" fill="var(--livery-white)"/>
  <polygon points="0,0 480,0 540,40 0,40" fill="var(--livery-red)"/>
  <polygon points="0,22 400,40 380,80 0,62" fill="var(--livery-black)"/>
  <text class="t-head" x="200" y="58" font-size="14" fill="#fff" letter-spacing="2" text-anchor="middle" transform="rotate(3 200 58)">WWW.BRAMBLEPEAKTYRES.CO.UK</text>
  <circle cx="60" cy="100" r="30" fill="var(--livery-red)"/>
  <text class="t-head" x="105" y="120" font-size="42" fill="var(--ink)" transform="rotate(4 105 120)">BRAMBLE PEAK TYRES</text>
  <polygon points="0,150 660,196 660,232 0,186" fill="var(--livery-red)"/>
  <text class="t-body" x="230" y="190" font-size="17" fill="#fff" text-anchor="middle" transform="rotate(4 230 190)">“We save you time and money”</text>
  <polygon points="0,186 660,232 660,320 0,320" fill="var(--livery-dark)"/>
  <text class="t-head" x="200" y="222" font-size="15" fill="#fff" letter-spacing="1" text-anchor="middle" transform="rotate(4 200 222)">MOBILE TYRE FITTING</text>
  <text class="t-head" x="500" y="174" font-size="22" fill="var(--livery-red)" transform="rotate(4 500 174)">07700 <tspan fill="var(--ink)">900 462</tspan></text>
</svg>

<!-- Rear doors -->
<svg class="panel panel--rear" viewBox="0 0 228 300" aria-label="Rear livery">
  <rect x="0" y="0" width="228" height="300" rx="14" fill="var(--livery-white)"/>
  <rect x="40" y="0" width="148" height="26" fill="var(--livery-red)"/>
  <text class="t-head" x="114" y="19" font-size="13" fill="#fff" text-anchor="middle" letter-spacing="1">MOBILE TYRE FITTING</text>
  <circle cx="34" cy="72" r="16" fill="var(--livery-red)"/>
  <text class="t-head" x="56" y="79" font-size="18" fill="var(--ink)">BRAMBLE PEAK TYRES</text>
  <text class="t-head" x="114" y="122" font-size="24" fill="var(--ink)" text-anchor="middle">07700 900 462</text>
  <polygon points="0,135 228,135 228,162 0,170" fill="var(--livery-red)"/>
  <text class="t-body" x="114" y="154" font-size="11" fill="#fff" text-anchor="middle">“We save you time and money”</text>
  <rect x="0" y="166" width="228" height="134" fill="var(--livery-dark)"/>
  <circle cx="28" cy="196" r="8" fill="#fff"/>
  <text class="t-body" x="42" y="199" font-size="7" fill="#fff">bramblepeaktyres</text>
  <text class="t-head" x="114" y="232" font-size="14" fill="#fff" text-anchor="middle" letter-spacing="1">WWW.BRAMBLEPEAKTYRES.CO.UK</text>
</svg>

<!-- Front -->
<svg class="panel panel--front" viewBox="0 0 260 287" aria-label="Front livery">
  <rect x="0" y="0" width="260" height="287" rx="16" fill="var(--livery-white)"/>
  <rect x="20" y="0" width="220" height="44" rx="10" fill="var(--livery-red)"/>
  <text class="t-head" x="130" y="31" font-size="21" fill="#fff" text-anchor="middle" letter-spacing="1">07700 900 462</text>
  <circle cx="72" cy="152" r="7" fill="var(--livery-red)"/>
  <text class="t-head" x="86" y="158" font-size="15" fill="var(--ink)">BRAMBLE PEAK TYRES</text>
  <rect x="0" y="190" width="260" height="97" fill="var(--livery-dark)"/>
</svg>

</body>
</html>
```